Creation of a book cover
Size : 14 x 20,5 cm (+ 5 mm bleed area at the top, bottom and right areas)
The Title is a French sentence which means “The heron dreaming on the cold roof of this empty station”. It’s a surrealistic title which has no link to the story.
AUTHOR : Mathieu Vorlange
TITLE : "Le héron rêvant sur le toit froid de cette gare vide »
PUBLISHER (AT THE BOTTOM OF THE PAGE) : Editions Parvenche
I send a PDF file with the kind of cover we have imagine, but you can propose something different. The glass and the fly can of course be used.

```html
<!DOCTYPE html>
<html lang="fr">
<head>
<meta charset="utf-8">
<title>Le héron rêvant sur le toit froid de cette gare vide — Mathieu Vorlange</title>
<link rel="stylesheet" href="https://fonts.googleapis.com/css2?family=Bebas+Neue&family=Oswald:wght@400&family=Rubik+Dirt&family=Cabin:wght@400&display=swap">
<style>
  :root {
    --backdrop: #c3c3c3;
    --paper: #ffffff;
    --grid: #e2e2e2;
    --ink: #0d0d0d;
    --blood: #860506;
  }
  html, body {
    margin: 0;
    padding: 0;
    width: 1200px;
    height: 1200px;
    overflow: hidden;
    background: var(--backdrop);
  }
  .cover {
    position: absolute;
    left: 215px;
    top: 48px;
    width: 769px;
    height: 1104px;
    background-color: var(--paper);
    background-image:
      linear-gradient(to right, var(--grid) 1px, transparent 1px),
      linear-gradient(to bottom, var(--grid) 1px, transparent 1px);
    background-size: 38.4px 38.4px;
    background-position: 38px 34px;
  }
  .author {
    position: absolute;
    top: 150px;
    left: 0;
    width: 100%;
    text-align: center;
    font-family: "Oswald", sans-serif;
    font-weight: 400;
    font-size: 38px;
    letter-spacing: 2px;
    color: var(--ink);
    margin: 0;
  }
  .title {
    position: absolute;
    top: 340px;
    left: 0;
    width: 100%;
    margin: 0;
    text-align: center;
    font-weight: 400;
  }
  .title-lead {
    display: block;
    font-family: "Rubik Dirt", sans-serif;
    font-size: 84px;
    line-height: 110px;
    color: var(--blood);
    letter-spacing: 1px;
  }
  .title-rest {
    display: block;
    font-family: "Bebas Neue", sans-serif;
    font-size: 72px;
    line-height: 66px;
    color: var(--ink);
    margin-top: 6px;
  }
  .illustration {
    position: absolute;
    left: 297px;
    top: 688px;
    width: 176px;
    height: 230px;
    border-radius: 10px 10px 22px 22px;
    background: linear-gradient(to bottom, #f2f5f5 0%, #cdd6d8 45%, #a9b6b9 80%, #7f8b8e 100%);
  }
  .publisher {
    position: absolute;
    top: 1000px;
    left: 0;
    width: 100%;
    text-align: center;
    font-family: "Cabin", sans-serif;
    font-size: 26px;
    color: var(--ink);
    margin: 0;
  }
</style>
</head>
<body>
  <main class="cover">
    <p class="author">Mathieu Vorlange</p>
    <h1 class="title">
      <span class="title-lead">LE HÉRON</span>
      <span class="title-rest">RÊVANT SUR LE TOIT FROID<br>DE CETTE GARE VIDE</span>
    </h1>
    <div class="illustration" role="img" aria-label="Illustration d’un verre d’eau avec une mouche posée sur le bord"></div>
    <p class="publisher">Éditions Parvenche</p>
  </main>
</body>
</html>
```